Business Card design for an International Import Export House

We need a Business Card design for our import export business. We trade in Minerals, Metals, Rice, Sugar, Steel etc.. The design should be minimalistic. It may or may not contain the physical address. In case you want to include the physical address - 418 Verandah Heights, Marlow Sector 9, Gurgaon, Haryana, India, 122009.

Target Market(s)

Steel Mills or Steel Plants, Factories, Mining businesses, Industrial houses, Government Agencies

Industry/Entity Type

Importer

Contact Information for Business Card

Business Name - Varden Overseas

Font styles to use
Other font styles liked:
• montserrat

Requirements
Must have
• Ravi Kandola - President
• www.vardenoverseas.com
• ravi@vardenoverseas.com
• +91-987-654-3217
Nice to have
• worldwide suppliers of ores

```html
<!DOCTYPE html>
<html lang="en">
<head>
<meta charset="utf-8">
<title>Varden Overseas — Business Card</title>
<link href="https://fonts.googleapis.com/css2?family=Lato:wght@400;700&family=Montserrat:wght@700&display=swap" rel="stylesheet">
<style>
  :root {
    --teal-deep: #2f7a94;
    --teal-light: #3e97a9;
    --teal-text: #2e7690;
    --paper: #f1f1f2;
    --ink: #3a3a3c;
    --backdrop: #cfcfd1;
  }
  * { margin: 0; padding: 0; box-sizing: border-box; }
  html, body {
    width: 1200px;
    height: 1129px;
    overflow: hidden;
    background: var(--backdrop);
  }
  .sheet {
    position: relative;
    width: 1200px;
    height: 1129px;
    display: flex;
    align-items: center;
    justify-content: center;
    gap: 40px;
  }
  .card {
    position: relative;
    width: 520px;
    height: 298px;
    overflow: hidden;
  }
  .card--front {
    background: linear-gradient(100deg, var(--teal-deep) 0%, var(--teal-light) 100%);
    display: flex;
    flex-direction: column;
    align-items: center;
    justify-content: center;
  }
  .brand {
    display: flex;
    align-items: center;
    gap: 12px;
  }
  .brand__dot {
    width: 18px;
    height: 18px;
    border-radius: 50%;
    background: #ffffff;
  }
  .brand__name {
    font-family: "Montserrat", sans-serif;
    font-weight: 700;
    font-size: 24px;
    letter-spacing: -0.5px;
    color: #ffffff;
    text-transform: uppercase;
  }
  .card--back {
    background: var(--paper);
    padding: 56px 0 0 56px;
  }
  .person__name {
    font-family: "Lato", sans-serif;
    font-weight: 700;
    font-size: 22px;
    color: var(--teal-text);
    line-height: 1;
  }
  .person__role {
    font-family: "Lato", sans-serif;
    font-weight: 400;
    font-size: 14px;
    color: var(--ink);
    margin-top: 6px;
  }
  .divider {
    width: 60px;
    height: 1px;
    background: var(--ink);
    margin-top: 52px;
  }
  .contact {
    list-style: none;
    margin-top: 58px;
  }
  .contact__item {
    display: flex;
    align-items: center;
    gap: 8px;
    font-family: "Lato", sans-serif;
    font-size: 14px;
    color: var(--ink);
    line-height: 19px;
  }
  .contact__icon {
    width: 10px;
    height: 10px;
    flex: none;
    fill: var(--teal-text);
  }
</style>
</head>
<body>
<main class="sheet">
  <section class="card card--front" aria-label="Card front">
    <div class="brand">
      <span class="brand__dot"></span>
      <span class="brand__name">Varden Overseas</span>
    </div>
  </section>

  <section class="card card--back" aria-label="Card back">
    <h1 class="person__name">Ravi Kandola</h1>
    <p class="person__role">President</p>
    <div class="divider"></div>
    <ul class="contact">
      <li class="contact__item">
        <svg class="contact__icon" viewBox="0 0 10 10" aria-hidden="true"><path d="M2 0.5 L3.6 2.6 L2.8 3.6 Q4 6 6.4 7.2 L7.4 6.4 L9.5 8 L8.4 9.5 Q4.5 9.5 1.8 6.4 Q0.5 4.4 0.5 1.6 Z"/></svg>
        +91-987-654-3217
      </li>
      <li class="contact__item">
        <svg class="contact__icon" viewBox="0 0 10 10" aria-hidden="true"><path d="M0.5 2 H9.5 V8.5 H0.5 Z M1.2 2.6 L5 5.6 L8.8 2.6" stroke="#f1f1f2" stroke-width="0.8"/></svg>
        ravi@vardenoverseas.com
      </li>
      <li class="contact__item">
        <svg class="contact__icon" viewBox="0 0 10 10" aria-hidden="true"><circle cx="5" cy="5" r="4.5"/><path d="M0.5 5 H9.5 M5 0.5 Q2.5 5 5 9.5 M5 0.5 Q7.5 5 5 9.5" stroke="#f1f1f2" stroke-width="0.7" fill="none"/></svg>
        www.vardenoverseas.com
      </li>
    </ul>
  </section>
</main>
</body>
</html>
```